U.S. Popcorn company needs business cards

We are a popcorn company that manufactures popcorn and sells it to grocery stores worldwide. Our theme is "Americana" and our logo is U.S. route 66 which is the most famous highway in the U.S.

We would like the design to be simple and to use both sides. On the back side we would like to see just the logo and website. The front would be normal details

Target Market(s)

Wholesalers, grocers and distributors

Industry/Entity Type

Manufacture

Contact Information for Business Card

Business name: Bluebell Ridge Popcorn
Phone: +1 555 014 2286
Email: Derek@bluebellridgepopcorn.com
website: www.bluebellridgepopcorn.com
Tag Line: "Freshly popped daily"
Name: Derek Halvorsen
Title: Founder/President

Requirements
Must have
• Either this design should be fun or clean and simple. I will let you show me your thougths.
Nice to have
• Anything that ties in the real Hwy Route 66.
• Colors might need to be red, white and blue incorporated.
Should not have
• Not be too busy.

```html
<!DOCTYPE html>
<html lang="en">
<head>
<meta charset="utf-8">
<title>Bluebell Ridge Popcorn – Business Cards</title>
<link href="https://fonts.googleapis.com/css2?family=Oswald:wght@600&family=Poppins:ital,wght@0,400;0,600;0,700;1,600&display=swap" rel="stylesheet">
<style>
  :root {
    --navy: #22306a;
    --red: #e3252b;
    --white: #ffffff;
    --ink: #1c1c1c;
    --grey: #5a5a5a;
    --backdrop: #ebebeb;
  }
  * { box-sizing: border-box; margin: 0; padding: 0; }
  html, body { width: 1200px; height: 1200px; overflow: hidden; }
  body {
    background: var(--backdrop);
    font-family: "Poppins", sans-serif;
    position: relative;
  }
  .card {
    position: absolute;
    left: 180px;
    width: 840px;
    height: 480px;
    background: var(--white);
    overflow: hidden;
    box-shadow: 0 6px 18px rgba(0,0,0,0.12);
  }
  .card--back { top: 80px; }
  .card--front { top: 640px; }

  /* Back side */
  .back__rule {
    position: absolute; left: 0; right: 0; top: 30px;
    height: 7px; background: var(--red);
  }
  .wordmark {
    display: flex; align-items: center; gap: 16px;
    color: var(--navy);
    font-family: "Poppins", sans-serif;
    font-weight: 700;
  }
  .wordmark__dot {
    border-radius: 50%;
    background: var(--red);
    flex: none;
  }
  .back__wordmark {
    position: absolute; left: 0; right: 0; top: 140px;
    justify-content: center;
    font-size: 44px;
  }
  .back__wordmark .wordmark__dot { width: 40px; height: 40px; }
  .back__band {
    position: absolute; left: 0; right: 0; bottom: 0;
    height: 190px; background: var(--navy);
    display: flex; align-items: center; justify-content: center;
  }
  .back__url {
    color: var(--white);
    font-size: 34px;
    font-weight: 600;
    letter-spacing: 1px;
  }

  /* Front side */
  .front__header {
    position: absolute; left: 50px; top: 40px;
    display: flex; align-items: flex-start; gap: 22px;
  }
  .company { width: 460px; }
  .company__name {
    font-family: "Oswald", sans-serif;
    font-weight: 600;
    font-size: 36px;
    text-transform: uppercase;
    color: var(--ink);
    line-height: 1.1;
    padding-bottom: 4px;
    border-bottom: 4px solid var(--red);
  }
  .company__tagline {
    text-align: right;
    font-style: italic;
    font-weight: 600;
    font-size: 24px;
    color: var(--ink);
    margin-top: 4px;
  }
  .front__wordmark {
    font-size: 20px;
    line-height: 1.15;
    margin-top: 4px;
  }
  .front__wordmark .wordmark__dot { width: 24px; height: 24px; }
  .person {
    position: absolute; left: 50px; top: 200px;
  }
  .person__name {
    font-size: 50px;
    font-weight: 700;
    color: var(--ink);
    line-height: 1.1;
  }
  .person__title {
    font-size: 24px;
    color: var(--grey);
    margin-top: 2px;
  }
  .contact {
    list-style: none;
    margin-top: 16px;
  }
  .contact__item {
    display: flex; align-items: center; gap: 16px;
    font-size: 23px;
    color: var(--ink);
    margin-bottom: 10px;
  }
  .contact__icon { width: 36px; height: 36px; flex: none; }
  .front__band {
    position: absolute; left: 0; right: 0; bottom: 16px;
    height: 26px; background: var(--navy);
  }
</style>
</head>
<body>

  <section class="card card--back" aria-label="Business card back">
    <div class="back__rule"></div>
    <div class="wordmark back__wordmark">
      <span class="wordmark__dot"></span>
      <span>Bluebell Ridge Popcorn</span>
    </div>
    <div class="back__band">
      <span class="back__url">www.bluebellridgepopcorn.com</span>
    </div>
  </section>

  <section class="card card--front" aria-label="Business card front">
    <header class="front__header">
      <div class="company">
        <h1 class="company__name">Bluebell Ridge Popcorn</h1>
        <p class="company__tagline">Freshly popped daily</p>
      </div>
      <div class="wordmark front__wordmark">
        <span class="wordmark__dot"></span>
        <span>Bluebell Ridge<br>Popcorn</span>
      </div>
    </header>

    <div class="person">
      <h2 class="person__name">Derek Halvorsen</h2>
      <p class="person__title">Founder/President</p>
      <ul class="contact">
        <li class="contact__item">
          <svg class="contact__icon" viewBox="0 0 36 36" aria-hidden="true">
            <circle cx="18" cy="18" r="18" fill="#e3252b"/>
            <path d="M12 10c1-1 2.5-1 3.2 0l1.8 2.6c.6.9.4 2-.4 2.6l-1.2.9c.9 2 2.5 3.7 4.5 4.6l.9-1.2c.6-.8 1.7-1 2.6-.4l2.6 1.8c1 .7 1 2.2 0 3.2l-1.3 1.3c-1.2 1.2-3.1 1.4-4.6.6C15.5 24 12 20.5 10.1 16.9c-.8-1.5-.6-3.4.6-4.6z" fill="#ffffff"/>
          </svg>
          <span>+1 555 014 2286</span>
        </li>
        <li class="contact__item">
          <svg class="contact__icon" viewBox="0 0 36 36" aria-hidden="true">
            <circle cx="18" cy="18" r="18" fill="#e3252b"/>
            <rect x="9" y="12" width="18" height="12" rx="1.5" fill="#ffffff"/>
            <path d="M9.5 12.8 18 19l8.5-6.2" fill="none" stroke="#e3252b" stroke-width="1.6"/>
          </svg>
          <span>Derek@bluebellridgepopcorn.com</span>
        </li>
      </ul>
    </div>

    <div class="front__band"></div>
  </section>

</body>
</html>
```